UX Design for Analytics Web Application

http://torvikgrove.com/
We are tech & consulting company with analytics products (web applications), located at Rio de Janeiro, Brazil.

We are searching a partner do develop UX for our products, i.e, aesthetics, usability, HTML/CSS.

Currently we have a product suite and the goal is to make a pilot re-design project with one of our products.

The product of interest is interactive webapp that aims at data analysis, significantly different from blogs, e-commerce or landing pages.

We do have a software development team but we lack an UX & HTML expert. Currently we use Bootstrap templates but the results are insatisfatory.

So, the project scope is, to develop the arts (UX, aesthetics, etc) along with the code/mockup (HTML/CSS) for one of our product (3 pages).

This is a pilot project and there's potential to rehire for our other products. Code quality is of importance.

More details and specification can be found in attached files.

Target Market(s)

Executives, managers & consultants

Industry/Entity Type

It Company

Coding

Coded - Design and coding required

Number of Pages Required

3 page

Font styles to use
Sans Serif

Requirements
Must have
• (see attached files, prefer the pptx version))
• -Responsive
Nice to have
• (see attached files, prefer the pptx version)
Should not have
• -Avoid Green, Red and Yellow colors. They have a meaning of good, bad and average in our products.

```html
<!DOCTYPE html>
<html lang="en">
<head>
<meta charset="utf-8">
<title>Torvik Gauge – Processes Dashboard</title>
<link href="https://fonts.googleapis.com/css2?family=Lato:wght@400;700&display=swap" rel="stylesheet">
<style>
:root{
  --ink:#33333f;
  --ink-soft:#4a4a52;
  --rust:#a8603c;
  --tan:#d6b396;
  --tan-light:#e4c8ae;
  --panel:#f7eadb;
  --white:#ffffff;
  --text:#3a3a44;
  --muted:#5a5a62;
}
*{box-sizing:border-box;margin:0;padding:0}
html,body{width:1200px;height:802px;overflow:hidden}
body{font-family:'Lato',sans-serif;color:var(--text);position:relative;
  background:linear-gradient(135deg,#f4e5d2 0%,#e8cdb1 45%,#c98e66 80%,#a85c36 100%)}
.abs{position:absolute}
.topbar{left:0;top:0;width:1200px;height:42px;background:var(--ink)}
.topbar .menu{left:16px;top:15px;width:12px}
.menu span{display:block;height:2px;background:#fff;margin-bottom:3px}
.brand{color:#fff;font-weight:400;letter-spacing:.2px}
.topbar .brand{left:60px;top:10px;font-size:19px}
.tools{right:43px;top:0;height:42px;display:flex}
.tool{width:38px;height:42px;border-left:1px solid #45454f;display:flex;align-items:center;justify-content:center;position:relative}
.tool:last-child{border-right:1px solid #45454f}
.badge{position:absolute;top:9px;right:8px;width:11px;height:11px;border-radius:50%;background:var(--rust);color:#fff;font-size:6px;display:flex;align-items:center;justify-content:center}
.section-title{font-size:12px;color:var(--muted);display:flex;align-items:center;gap:8px}
.section-title svg{width:15px;height:15px}
.panel{background:var(--panel)}
.overview{left:44px;top:78px;width:695px;height:199px}
.overview h1{left:32px;top:18px;font-size:20px;font-weight:700;color:var(--text)}
.row-label{left:32px;color:var(--text)}
.row-label b{font-weight:700}
.bar{height:18px;font-size:11px;color:#fff;text-align:right;padding-right:7px;line-height:18px}
.bar.dark{background:repeating-linear-gradient(-45deg,#2f2f3b 0 2px,#4a4a58 2px 4px)}
.bar.rust{background:var(--rust)}
.bar.white{background:#fff;color:var(--text)}
.pct{left:609px;top:121px;font-size:32px;font-weight:700;color:var(--text);line-height:1}
.pct sup{font-size:18px;vertical-align:top}
.pct-label{left:608px;top:156px;font-size:12px}
.feed{left:774px;top:78px;width:383px;height:199px}
.feed-item{left:24px;width:344px;display:flex;align-items:center;gap:16px;font-size:9px;line-height:1.35;color:var(--text)}
.feed-item svg{flex-shrink:0}
.feed-item span{width:222px}
.feed-item u{text-decoration:underline}
.feed-sep{left:18px;width:348px;height:1px;background:#e6d6c4}
.btn{left:16px;top:156px;width:351px;height:28px;background:var(--rust);color:#fff;font-size:14px;text-align:center;line-height:28px;border-radius:2px}
.controls{left:44px;top:312px;width:1113px;height:164px}
.search{left:34px;top:30px;width:246px;height:37px;border-bottom:1px solid #8a8a90;font-size:11px;line-height:37px;padding-left:1px}
.search svg{position:absolute;right:7px;top:12px}
.select{top:30px;width:247px;height:37px;background:#fff;font-size:11px;line-height:37px;padding-left:12px}
.select .caret{position:absolute;right:0;top:0;width:37px;height:37px;background:var(--tan);display:flex;align-items:center;justify-content:center}
.track{height:1px;background:#8a8a90;top:106px}
.track-fill{height:3px;background:var(--ink);top:105px}
.thumb{width:16px;height:16px;border-radius:50%;background:var(--ink);top:98px}
.tip{top:127px;width:61px;height:17px;background:var(--ink);color:#fff;font-size:11px;text-align:center;line-height:17px}
.tip::before{content:"";position:absolute;left:27px;top:-4px;border:3.5px solid transparent;border-top:0;border-bottom:4px solid var(--ink)}
.cardlist{left:44px;top:512px;width:1113px;height:224px}
.card{top:24px;width:335px;height:176px;background:#fff;border:1px solid #ecdccb}
.card-media{left:0;top:0;width:100%;height:65px}
.card-media h2{position:absolute;left:18px;top:35px;color:#fff;font-size:18px;font-weight:700;letter-spacing:-.3px}
.card-stat{left:18px;top:82px;display:flex;align-items:center;gap:10px;font-size:18px}
.card-text{left:20px;top:120px;font-size:11.5px;line-height:1.45}
.card-text u{text-decoration:underline}
.card-text b{font-weight:700}
.card-chart{right:16px;top:78px}
.footer{left:0;top:764px;width:1200px;height:38px;background:var(--ink-soft)}
.footer .brand{left:886px;top:11px;font-size:14px}
</style>
</head>
<body>
<svg width="0" height="0" class="abs">
  <defs>
    <pattern id="hatch" width="4" height="4" patternUnits="userSpaceOnUse" patternTransform="rotate(45)">
      <rect width="4" height="4" fill="#2f2f3b"/><rect width="2" height="4" fill="#4a4a58"/>
    </pattern>
  </defs>
</svg>

<header class="topbar abs">
  <div class="menu abs"><span></span><span></span><span></span></div>
  <div class="brand abs">Torvik Gauge</div>
  <div class="tools abs">
    <div class="tool"><svg width="13" height="14" viewBox="0 0 13 14"><path d="M6.5 1a4 4 0 0 1 4 4v4l1.5 2H1l1.5-2V5a4 4 0 0 1 4-4z" fill="#fff"/><circle cx="6.5" cy="12.5" r="1.5" fill="#fff"/></svg><span class="badge">10</span></div>
    <div class="tool"><svg width="13" height="14" viewBox="0 0 13 14"><circle cx="6.5" cy="4" r="3.2" fill="#fff"/><path d="M0 14c0-4 3-6 6.5-6S13 10 13 14z" fill="#fff"/></svg><span class="badge">6</span></div>
    <div class="tool"><svg width="22" height="14" viewBox="0 0 22 14"><circle cx="7" cy="7" r="4.5" fill="none" stroke="#fff" stroke-width="3" stroke-dasharray="2.4 1.3"/><circle cx="7" cy="7" r="3" fill="#fff"/><circle cx="7" cy="7" r="1.3" fill="#33333f"/><path d="M17 6h4l-2 2z" fill="#fff"/></svg></div>
  </div>
</header>

<div class="section-title abs" style="left:44px;top:55px">
  <svg viewBox="0 0 15 15"><rect x="3" y="1" width="10" height="13" fill="none" stroke="#666"/><path d="M5 4h6M5 7h6M5 10h6" stroke="#666"/></svg>Processes Overview</div>
<div class="section-title abs" style="left:774px;top:55px">
  <svg viewBox="0 0 15 15"><path d="M1 3h12M1 7h12M1 11h12" stroke="#555" stroke-width="2"/></svg>Activity Feed</div>

<section class="overview panel abs">
  <h1 class="abs">14 Active Processes</h1>
  <div class="row-label abs" style="top:64px;font-size:17px">31 millions <b>expent</b></div>
  <div class="bar dark abs" style="left:190px;top:67px;width:162px">?</div>
  <div class="row-label abs" style="top:109px;font-size:14px">with 2 millions of <b style="color:var(--rust)">gap</b></div>
  <div class="bar rust abs" style="left:190px;top:109px;width:213px">6%</div>
  <div class="row-label abs" style="top:153px;font-size:11px">and 1.5 million <b>negotiated</b></div>
  <div class="bar white abs" style="left:190px;top:150px;width:179px">5%</div>
  <svg class="abs" style="left:435px;top:27px" width="146" height="146" viewBox="0 0 146 146">
    <circle cx="73" cy="73" r="71.5" fill="none" stroke="#33333f" stroke-width="1.6" stroke-dasharray="3 2.5"/>
    <g transform="rotate(-90 73 73)" fill="none" stroke-width="23">
      <circle cx="73" cy="73" r="51.5" stroke="#fff"/>
      <circle cx="73" cy="73" r="51.5" stroke="url(#hatch)" stroke-dasharray="233 400"/>
      <circle cx="73" cy="73" r="51.5" stroke="#a8603c" stroke-dasharray="0 233 52 400"/>
    </g>
  </svg>
  <div class="pct abs">72<sup>%</sup></div>
  <div class="pct-label abs">Completed</div>
</section>

<section class="feed panel abs">
  <div class="feed-item abs" style="top:15px"><svg width="30" height="30"><circle cx="15" cy="15" r="12.5" fill="none" stroke="#33333f" stroke-width="4"/></svg><span><u>Lena Markov</u> upload new data with 23823 rows to the <u>XPTO Process</u> and he is happy now &nbsp;&nbsp;- 2 days ago</span></div>
  <div class="feed-sep abs" style="top:51px"></div>
  <div class="feed-item abs" style="top:63px"><svg width="30" height="30"><rect x="2" y="2" width="26" height="26" fill="none" stroke="#a8603c" stroke-width="4"/></svg><span><u>Otto Brandt</u> started the <u>ABC process</u> &nbsp;&nbsp;- 2 days ago</span></div>
  <div class="feed-sep abs" style="top:104px"></div>
  <div class="feed-item abs" style="top:115px"><svg width="30" height="30"><path d="M15 3L28 28H2z" fill="none" stroke="#e4c8ae" stroke-width="4"/></svg><span><u>Iris Calloway</u> is making a new content layout<br>specification &nbsp;&nbsp;- 2 days ago</span></div>
  <div class="btn abs">Sell all</div>
</section>

<div class="section-title abs" style="left:42px;top:288px">
  <svg viewBox="0 0 15 15"><path d="M2 1v13M6 1v13M10 1v13M14 1v13" stroke="#555" stroke-width="1.4"/><path d="M0 5h4M4 10h4M8 4h4M12 9h3" stroke="#555" stroke-width="2"/></svg>Processes Cards List Control</div>

<section class="controls panel abs">
  <div class="search abs">Search<svg width="14" height="14"><circle cx="6" cy="6" r="4.5" fill="none" stroke="#33333f" stroke-width="1.6"/><path d="M9.5 9.5l3.5 3.5" stroke="#33333f" stroke-width="1.8"/></svg></div>
  <div class="select abs" style="left:299px">Sort By<span class="caret"><svg width="12" height="8"><path d="M1 1l5 5 5-5" fill="none" stroke="#fff" stroke-width="1.6"/></svg></span></div>
  <div class="select abs" style="left:566px">Filter By<span class="caret"><svg width="12" height="8"><path d="M1 1l5 5 5-5" fill="none" stroke="#fff" stroke-width="1.6"/></svg></span></div>
  <div class="select abs" style="left:833px">Add Process<span class="caret"><svg width="12" height="8"><path d="M1 1l5 5 5-5" fill="none" stroke="#fff" stroke-width="1.6"/></svg></span></div>

  <div class="track abs" style="left:34px;width:512px"></div>
  <div class="track-fill abs" style="left:34px;width:245px"></div>
  <div class="thumb abs" style="left:271px"></div>
  <div class="tip abs" style="left:249px">$120</div>

  <div class="track abs" style="left:566px;width:513px"></div>
  <div class="track-fill abs" style="left:641px;width:224px"></div>
  <div class="thumb abs" style="left:633px"></div>
  <div class="thumb abs" style="left:857px"></div>
  <div class="tip abs" style="left:611px">$50</div>
  <div class="tip abs" style="left:835px">$100</div>
</section>

<div class="section-title abs" style="left:42px;top:487px">
  <svg viewBox="0 0 15 15"><rect x="0.5" y="2.5" width="14" height="10" fill="none" stroke="#555"/><circle cx="4.5" cy="6.5" r="1.6" fill="#555"/><path d="M8 6h5M8 9h5M2.5 10.5h4" stroke="#555"/></svg>Processes Card List</div>

<section class="cardlist panel abs">
  <article class="card abs" style="left:29px">
    <div class="card-media abs" role="img" aria-label="Photo of power lines against a golden sunset sky" style="background:linear-gradient(100deg,#7a5a1c 0%,#c98a22 50%,#e3b02e 70%,#8f6a1f 100%)"><h2>Process Buy A Dount</h2></div>
    <div class="card-stat abs" style="color:var(--ink)"><svg width="32" height="32"><circle cx="16" cy="16" r="14.5" fill="none" stroke="#33333f" stroke-width="2"/><path d="M11 14l5 5 5-5" fill="none" stroke="#33333f" stroke-width="2"/></svg>14 million in expenses</div>
    <div class="card-text abs">Some short free text with <u>links</u> and<br><b>13,432 number</b></div>
    <svg class="card-chart abs" width="76" height="76" viewBox="0 0 76 76"><circle cx="38" cy="38" r="37" fill="none" stroke="#33333f" stroke-dasharray="2 2"/><g transform="rotate(-90 38 38)" fill="none" stroke-width="15"><circle cx="38" cy="38" r="27" stroke="#5a9bd5"/><circle cx="38" cy="38" r="27" stroke="#e4e4e4" stroke-dasharray="144 200"/><circle cx="38" cy="38" r="27" stroke="#e4c8ae" stroke-dasharray="119 200"/><circle cx="38" cy="38" r="27" stroke="#a8603c" stroke-dasharray="85 200"/><circle cx="38" cy="38" r="27" stroke="#33333f" stroke-dasharray="42 200"/></g></svg>
  </article>

  <article class="card abs" style="left:391px">
    <div class="card-media abs" role="img" aria-label="Photo of an empty industrial hall with tall windows" style="background:linear-gradient(180deg,#4d4640 0%,#8e8478 55%,#6e5a48 100%)"><h2>Process Buy A Dount</h2></div>
    <div class="card-stat abs" style="color:var(--rust)"><svg width="32" height="32"><circle cx="16" cy="16" r="14.5" fill="none" stroke="#a8603c" stroke-width="2"/><path d="M11 14l5 5 5-5" fill="none" stroke="#a8603c" stroke-width="2"/></svg>14 million in expenses</div>
    <div class="card-text abs">Some short free text with <u>links</u> and<br><b>13,432 number</b></div>
    <svg class="card-chart abs" width="76" height="76" viewBox="0 0 76 76"><circle cx="38" cy="38" r="37" fill="none" stroke="#33333f" stroke-dasharray="2 2"/><g transform="rotate(-90 38 38)" fill="none" stroke-width="15"><circle cx="38" cy="38" r="27" stroke="#5a9bd5"/><circle cx="38" cy="38" r="27" stroke="#e4e4e4" stroke-dasharray="144 200"/><circle cx="38" cy="38" r="27" stroke="#e4c8ae" stroke-dasharray="119 200"/><circle cx="38" cy="38" r="27" stroke="#a8603c" stroke-dasharray="85 200"/><circle cx="38" cy="38" r="27" stroke="#33333f" stroke-dasharray="42 200"/></g></svg>
  </article>

  <article class="card abs" style="left:753px">
    <div class="card-media abs" role="img" aria-label="Photo of brown leather shoes on a street" style="background:linear-gradient(100deg,#6a4a3a 0%,#8c5a3e 45%,#5a3424 70%,#7d6a5e 100%)"><h2>Process Buy A Dount</h2></div>
    <div class="card-stat abs" style="color:var(--tan-light)"><svg width="32" height="32"><circle cx="16" cy="16" r="14.5" fill="none" stroke="#e4c8ae" stroke-width="2"/><path d="M11 14l5 5 5-5" fill="none" stroke="#e4c8ae" stroke-width="2"/></svg>14 million in expenses</div>
    <div class="card-text abs">Some short free text with <u>links</u> and<br><b>13,432 number</b></div>
    <svg class="card-chart abs" width="76" height="76" viewBox="0 0 76 76"><circle cx="38" cy="38" r="37" fill="none" stroke="#33333f" stroke-dasharray="2 2"/><g transform="rotate(-90 38 38)" fill="none" stroke-width="15"><circle cx="38" cy="38" r="27" stroke="#5a9bd5"/><circle cx="38" cy="38" r="27" stroke="#e4e4e4" stroke-dasharray="144 200"/><circle cx="38" cy="38" r="27" stroke="#e4c8ae" stroke-dasharray="119 200"/><circle cx="38" cy="38" r="27" stroke="#a8603c" stroke-dasharray="85 200"/><circle cx="38" cy="38" r="27" stroke="#33333f" stroke-dasharray="42 200"/></g></svg>
  </article>
</section>

<footer class="footer abs">
  <div class="brand abs">Torvik</div>
</footer>
</body>
</html>
```